Business card design needed

Financial planning company that specialises in super and insurance

I have attached my email with my logo so if you incorporate the logo please

Industry/Entity Type

Business

Contact Information for Business Card

Derek Hollis AFP AFFS(FP) ( regisestered trademark of the p on afp)
Financial Planner

m 0412 564 918
p 1300 426 715
f 02 9638 1407
e derek@tbplanners.com.au
www. tbplanners.com.au

Suite 4 /9 Marlowe Crescent
Kestrel Point NSW 2536

Suite 1703 Level 17 North Block,
Harbourgate Plaza Centre
214 Ketley Road NSW 2031

Logo Text

Tidewater Bay Planners

Logo styles of interest
Pictorial/Combination Logo
Requirements
Must have
• muST logo can be rejigged but must keep opera house

```html
<!DOCTYPE html>
<html lang="en">
<head>
<meta charset="utf-8">
<title>Tidewater Bay Planners – Business Card</title>
<link rel="stylesheet" href="https://fonts.googleapis.com/css2?family=Montserrat:wght@300;400;600;700&display=swap">
<style>
  :root {
    --page-bg: #ffffff;
    --ink: #1f1f1f;
    --ink-soft: #333333;
    --brand-green: #00c800;
    --bar-dark: #2a2a2a;
    --silver-1: #d6d6d6;
    --silver-2: #f6f6f6;
    --silver-3: #cdcdcd;
    --card-edge: #dcdcdc;
  }
  html, body {
    margin: 0;
    width: 1200px;
    height: 726px;
    overflow: hidden;
    background: var(--page-bg);
    font-family: "Montserrat", sans-serif;
    color: var(--ink);
  }
  .business-card {
    position: absolute;
    left: 120px;
    top: 95px;
    width: 914px;
    height: 508px;
    border: 1px solid var(--card-edge);
    box-sizing: border-box;
    overflow: hidden;
    background:
      linear-gradient(115deg, rgba(255,255,255,0) 30%, rgba(255,255,255,0.7) 45%, rgba(255,255,255,0) 58%),
      linear-gradient(160deg, var(--silver-1) 0%, var(--silver-2) 45%, var(--silver-3) 100%);
  }
  .brand-name {
    position: absolute;
    left: 470px;
    top: 128px;
    display: flex;
    align-items: center;
    gap: 12px;
    font-weight: 700;
    font-size: 26px;
    letter-spacing: 0.5px;
    color: var(--ink);
    white-space: nowrap;
  }
  .brand-square {
    width: 22px;
    height: 22px;
    background: var(--brand-green);
  }
  .person-name {
    position: absolute;
    left: 84px;
    top: 124px;
    margin: 0;
    font-size: 26px;
    font-weight: 700;
    color: var(--ink);
  }
  .person-name .credential {
    font-weight: 400;
    font-size: 23px;
  }
  .person-name sup { font-size: 12px; }
  .person-role {
    position: absolute;
    left: 84px;
    top: 165px;
    margin: 0;
    font-size: 21px;
    font-weight: 300;
    color: var(--ink-soft);
  }
  .contact-list {
    position: absolute;
    left: 50px;
    top: 262px;
    margin: 0;
    padding: 0;
    list-style: none;
  }
  .contact-list li {
    display: flex;
    align-items: center;
    height: 35px;
    font-size: 22px;
    font-weight: 300;
    color: var(--ink-soft);
  }
  .contact-icon {
    width: 20px;
    height: 20px;
    margin-right: 13px;
    fill: none;
    stroke: var(--ink-soft);
    stroke-width: 1.6;
  }
  .office-address {
    position: absolute;
    left: 433px;
    margin: 0;
    font-style: normal;
    font-size: 19px;
    font-weight: 300;
    line-height: 24px;
    color: var(--ink-soft);
    white-space: nowrap;
  }
  .office-address.primary { top: 262px; }
  .office-address.secondary { top: 326px; }
  .card-bands {
    position: absolute;
    left: 0;
    bottom: 0;
    width: 914px;
    height: 62px;
  }
  .website {
    position: absolute;
    left: 86px;
    top: 455px;
    margin: 0;
    font-size: 22px;
    font-weight: 700;
    letter-spacing: 0.5px;
    color: var(--ink);
  }
</style>
</head>
<body>
  <section class="business-card">
    <div class="brand-name"><span class="brand-square"></span>Tidewater Bay Planners</div>

    <h1 class="person-name">Derek Hollis <span class="credential">AFP<sup>®</sup></span></h1>
    <p class="person-role">Financial Planner</p>

    <ul class="contact-list">
      <li>
        <svg class="contact-icon" viewBox="0 0 20 20"><rect x="5" y="2" width="10" height="16" rx="1.5"/><line x1="8.5" y1="15" x2="11.5" y2="15"/></svg>
        0412 564 918
      </li>
      <li>
        <svg class="contact-icon" viewBox="0 0 20 20"><path d="M5 2.5l3 3-1.8 2.2c1 2.3 2.8 4.1 5.1 5.1L13.5 11l3 3-2 2.5C8.5 16 4 11.5 3.5 5.5z"/></svg>
        1300 426 715
      </li>
      <li>
        <svg class="contact-icon" viewBox="0 0 20 20"><rect x="6" y="2" width="8" height="5"/><rect x="2.5" y="7" width="15" height="8" rx="1"/><rect x="5" y="12" width="10" height="6"/></svg>
        02 9638 1407
      </li>
      <li>
        <svg class="contact-icon" viewBox="0 0 20 20"><rect x="2" y="5" width="16" height="11"/><polyline points="2,5 10,11 18,5"/></svg>
        derek@tbplanners.com.au
      </li>
    </ul>

    <address class="office-address primary">
      Suite 4/9 Marlowe Crescent Kestrel Point<br>NSW 2536
    </address>
    <address class="office-address secondary">
      Suite 1703 Level 17 North Block,<br>
      Harbourgate Plaza Centre 214 Ketley Road<br>
      NSW 2031
    </address>

    <svg class="card-bands" viewBox="0 446 914 62" preserveAspectRatio="none" aria-hidden="true">
      <polygon points="434,446 914,446 914,469 465,469" fill="var(--bar-dark)"/>
      <polygon points="0,446 402,446 460,479 914,479 914,508 0,508" fill="var(--brand-green)"/>
    </svg>
    <p class="website">www.tbplanners.com.au</p>
  </section>
</body>
</html>
```